Intermodal Trucking Company Website

My client is a trucking company that takes the containers you see on the back of a ship or railroad car and delivers them in the midwestern part of the United States. Here are some of their competitors Websites and their logo to use as part of the design.

http://www.varnekhaulers.example/
https://www.plirext.example/
http://www.brontagefreight.example/
https://www.lqp-xy.example/

Industry/Entity Type

Trucking Company

Number of Pages Required

2 page

Requirements
Must have
• Website must be professional and the design needs to be suitable for a responsive Website.
Should not have
• Please do not submit designs with misspellings. Designs with misspellings will be eliminated.

```html
<!DOCTYPE html>
<html lang="en">
<head>
<meta charset="utf-8">
<title>Tandem R.R. Inc. – Website Design</title>
<link rel="stylesheet" href="https://fonts.googleapis.com/css2?family=Roboto:wght@400;500;700;900&family=Roboto+Condensed:wght@400;700&display=swap">
<style>
:root{
  --stage:#8b8b8b;
  --white:#ffffff;
  --black:#0d0d0d;
  --red:#b00a0a;
  --red-text:#c41a12;
  --orange:#f59d1f;
  --orange-text:#f5a623;
  --gray-bg:#e4e4e4;
  --text:#4a4a4a;
  --dark:#1e1e1e;
  --input:#fbe3e0;
}
*{box-sizing:border-box;margin:0;padding:0}
html,body{width:1200px;height:1200px;overflow:hidden}
body{background:var(--stage);font-family:"Roboto",sans-serif;color:var(--text);position:relative}
.page{position:absolute;width:520px;background:var(--white);overflow:hidden}
.page--home{left:36px;top:33px;height:1142px}
.page--about{left:636px;top:33px;height:962px;width:519px}
.abs{position:absolute}

/* header */
.site-header{left:0;top:0;width:100%;height:45px;background:var(--white)}
.brand{display:flex;align-items:center;gap:3px;font-weight:700;font-size:8px;color:var(--red)}
.brand-dot{width:9px;height:9px;border-radius:50%;background:var(--red)}
.contact-mini{display:flex;gap:5px;align-items:flex-start;font-size:5px;line-height:7px;color:#444}
.contact-mini svg{width:10px;height:10px;flex:none}

/* nav */
.main-nav{left:0;top:45px;width:100%;height:23px;background:var(--black)}
.nav-links{left:43px;top:8px;display:flex;gap:7px;font-size:6.5px;font-weight:700;color:var(--white)}
.nav-links .active{position:relative}
.nav-links .active::after{content:"";position:absolute;left:0;right:0;bottom:-5px;height:2px;background:var(--orange)}
.track{top:4px;height:15px;width:103px;border-radius:8px;background:var(--input);display:flex;overflow:hidden;font-size:6px}
.track span{flex:1;padding:4px 9px;color:#999}
.track b{background:var(--orange);color:var(--white);padding:4px 7px;font-weight:700}

/* hero */
.hero-photo{left:0;top:68px;width:100%;height:221px;background:linear-gradient(100deg,#2a2f38 0%,#5a4a48 30%,#8c3a34 50%,#5c5552 70%,#3a3d44 100%)}
.eyebrow{left:43px;top:119px;font-size:11px;font-weight:500;color:var(--orange-text)}
.hero-title{left:43px;top:148px;font-size:18px;font-weight:700;color:var(--white);letter-spacing:.2px}
.hero-sub{left:43px;top:173px;font-size:11.5px;font-weight:500;color:var(--white)}

.quote-form{left:352px;top:90px;width:132px;height:177px;background:var(--orange);border:2px solid #f8c47a;border-radius:3px}
.quote-form h3{position:absolute;left:8px;top:7px;font-family:"Roboto Condensed",sans-serif;font-size:13px;font-weight:700;color:var(--red-text);letter-spacing:-.3px}
.quote-form .field{position:absolute;left:8px;width:114px;height:16px;background:var(--input);border:1px solid #e6b7a9;font-size:6px;color:#999;padding:4px 5px}
.quote-form .submit{position:absolute;left:8px;top:143px;width:114px;height:17px;background:var(--red);color:var(--white);font-size:6.5px;font-weight:700;text-align:center;line-height:17px}

/* intro band */
.intro{left:0;top:289px;width:100%;height:122px;background:var(--red)}
.intro-copy{left:43px;top:298px;width:220px;font-size:7.3px;line-height:9.7px;color:var(--white);text-align:justify}
.intro-copy p+p{margin-top:9px}
.founder{margin-top:10px;font-weight:700}
.founder small{display:block;font-weight:400;font-size:6.5px;line-height:8px}
.video{left:307px;top:301px;width:176px;height:98px;background:linear-gradient(90deg,#e8e8e6,#cfcac3 50%,#efefee)}
.play{left:381px;top:340px;width:18px;height:18px}

/* pillars */
.pillars{left:0;top:411px;width:100%;height:213px;background:var(--gray-bg)}
.pillar{top:434px;width:140px}
.pillar h2{font-size:22px;font-weight:900;color:#111;letter-spacing:-1.2px;white-space:nowrap}
.pillar h4{margin-top:9px;font-size:10px;line-height:12px;font-weight:500;color:var(--red-text)}
.pillar p{margin-top:8px;font-size:7.3px;line-height:9.8px;color:#555}

/* services */
.services{left:0;top:624px;width:100%;height:206px;background:var(--orange)}
.service{left:55px;width:430px}
.service svg{position:absolute;left:0;top:0;width:44px;height:40px}
.service h3{position:absolute;left:59px;top:3px;font-size:11.5px;font-weight:700;color:var(--white);white-space:nowrap}
.service p{position:absolute;left:60px;top:21px;width:365px;font-size:7.3px;line-height:9.6px;color:#3a2a14}

/* footer */
.site-footer{left:0;width:100%;background:linear-gradient(160deg,#262626,#141414 55%,#202020)}
.footer-brand{flex-direction:column;font-size:8px;color:var(--orange-text);gap:4px;text-align:center;width:90px}
.footer-brand .brand-dot{width:12px;height:12px}
.f-label{font-size:7px;font-weight:700;color:var(--orange-text)}
.f-value{font-size:12px;line-height:15px;color:var(--white);margin-top:3px}
.f-links{display:flex;flex-direction:column;gap:10px;font-size:7.5px;font-weight:700;color:var(--orange-text)}
.social{display:flex;gap:10px}
.social span{width:24px;height:24px;border-radius:50%;background:#5a5a5a;border:2px solid #777}

/* about page */
.about-hero{left:0;top:68px;width:100%;height:121px;background:linear-gradient(180deg,#3a4050,#232836 60%,#1c2030)}
.about-title{left:43px;top:110px;font-size:24px;font-weight:900;color:var(--white);letter-spacing:-.3px}
.about-body{left:0;top:189px;width:100%;height:267px;background:var(--gray-bg)}
.section-title{font-size:15px;font-weight:700}
.truck-photo{left:43px;top:267px;width:186px;height:135px;background:linear-gradient(180deg,#f0f0f0,#cfd3d6 40%,#2f8a76 70%,#2a2a2a 92%,#e4e4e4)}
.about-copy{left:259px;top:255px;width:217px;font-size:7.3px;line-height:9.7px;color:#555}
.about-copy p+p{margin-top:9px}
.offer{left:0;top:456px;width:100%;height:190px;background:var(--orange)}
.offer-item{top:518px;width:150px;text-align:center}
.offer-item .icon{width:44px;height:44px;border-radius:50%;background:#f3efe8;border:2px solid #fff;margin:0 auto;display:flex;align-items:center;justify-content:center}
.offer-item h4{margin-top:10px;font-size:12px;font-weight:500;color:#2a1a08}
.offer-item p{margin-top:4px;font-size:7.3px;line-height:9.5px;color:#5a3c10}
</style>
</head>
<body>

<!-- HOME PAGE -->
<section class="page page--home">
  <header class="abs site-header">
    <div class="abs brand" style="left:36px;top:18px"><span class="brand-dot"></span>Tandem R.R.</div>
    <div class="abs contact-mini" style="left:212px;top:15px">
      <svg viewBox="0 0 10 10"><path d="M2 1l2 2-1 1.5c.6 1.2 1.4 2 2.5 2.5L7 6l2 2-1.3 1.3C4.5 9 1 5.5.7 2.3z" fill="none" stroke="#c41a12" stroke-width=".9"/></svg>
      <div>555-014-2290<br>enquire@tandemrr.example</div>
    </div>
    <div class="abs contact-mini" style="left:366px;top:15px">
      <svg viewBox="0 0 10 10"><path d="M5 9.5S1.8 6 1.8 4a3.2 3.2 0 016.4 0C8.2 6 5 9.5 5 9.5z" fill="none" stroke="#c41a12" stroke-width=".9"/><circle cx="5" cy="4" r="1.1" fill="#c41a12"/></svg>
      <div>718 Harlow Street<br>Kansas City, KS 66190</div>
    </div>
  </header>
  <nav class="abs main-nav">
    <div class="abs nav-links"><span class="active">HOME</span><span>COMPANY</span><span>SERVICES</span><span>NEWS</span><span>CONTACT</span></div>
    <div class="abs track" style="left:381px"><span>Enter Tracking ID</span><b>Track</b></div>
  </nav>

  <div class="abs hero-photo" role="img" aria-label="Red semi truck driving on a highway at dusk"></div>
  <div class="abs eyebrow">TANDEM R.R. INC.</div>
  <div class="abs hero-title">FAST - SECURED - RELIABLE</div>
  <div class="abs hero-sub">Transport &amp; Logistics Service</div>

  <form class="abs quote-form">
    <h3>Request a Free Quote</h3>
    <div class="field" style="top:28px">Company / Contact Name</div>
    <div class="field" style="top:51px">Phone</div>
    <div class="field" style="top:74px">Email</div>
    <div class="field" style="top:97px">Origin</div>
    <div class="field" style="top:120px">Destination</div>
    <div class="submit">Submit Information</div>
  </form>

  <div class="abs intro"></div>
  <div class="abs intro-copy">
    <p>Tandem R.R. Inc. was established with the sole aim of enabling growth, by providing efficient and prompt logistics, freight forwarding &amp; transportation solutions for Export/Import bound cargo.</p>
    <p>In addition, it also offers various other support services like warehousing, customs clearance and documentation, etc.</p>
    <div class="founder">Alan Merrow<small>Founder &amp; President</small></div>
  </div>
  <div class="abs video" role="img" aria-label="Video still of the company founder at his desk"></div>
  <svg class="abs play" viewBox="0 0 18 18"><circle cx="9" cy="9" r="8" fill="rgba(0,0,0,.35)" stroke="#fff" stroke-width="1.2"/><path d="M7 5.5v7l5.5-3.5z" fill="#fff"/></svg>

  <div class="abs pillars"></div>
  <div class="abs pillar" style="left:43px">
    <h2>WHO WE ARE</h2>
    <h4>Your Regional Transportation and Warehousing Specialist</h4>
    <p>Being Regional, we can assist you in finding a custom solution to your transportation or warehousing needs. From simple drayage or van load, to complex, multi-faceted problems, let us consolidate your solution efficiently.</p>
  </div>
  <div class="abs pillar" style="left:192px">
    <h2>WHAT WE DO</h2>
    <h4>Let us solve your warehouse or transportation problem</h4>
    <p>Our Regional coverage includes: Kansas, Missouri, Iowa, Nebraska, Illinois, South Dakota, Texas, Oklahoma,and Arkansas. In Kansas City, we service the following rail ramps: Plains Rail, QRT, KVR MN, BTRX and LPWD (Logistics Park Westdale).</p>
  </div>
  <div class="abs pillar" style="left:340px">
    <h2>WHY US</h2>
    <h4>We foster long term relationships</h4>
    <p>We are focused on providing quality customer service. By customizing your transportation or storage needs, we can help improve your bottom line. Our commitment to providing cost-effective custom solutions has allowed us to grow into a leading company in the Kansas City market.</p>
  </div>

  <div class="abs services"></div>
  <div class="abs service" style="top:647px">
    <svg viewBox="0 0 44 40"><rect x="8" y="4" width="28" height="26" rx="2" fill="var(--red)"/><rect x="12" y="9" width="20" height="8" fill="var(--orange)"/><rect x="6" y="30" width="32" height="4" fill="var(--red)"/><circle cx="13" cy="36" r="3" fill="var(--red)"/><circle cx="31" cy="36" r="3" fill="var(--red)"/></svg>
    <h3>TRUCKING SHIPPING SERVICES</h3>
    <p>When you ship by Tandem R.R. Inc, your shipment is handled and routed in the most efficient manner to arrive at its destination.</p>
  </div>
  <div class="abs service" style="top:708px">
    <svg viewBox="0 0 44 40"><rect x="2" y="12" width="26" height="16" fill="var(--red)"/><path d="M28 16h9l5 7v5H28z" fill="var(--red)"/><circle cx="10" cy="31" r="3.5" fill="var(--red)"/><circle cx="35" cy="31" r="3.5" fill="var(--red)"/></svg>
    <h3>SPECIALITY FREIGHT &amp; SHIPPING SERVICES</h3>
    <p>For the past 35 years, we've been arranging global freight solutions for businesses of all sizes. we are always striving to make our operations safer and more efficient.</p>
  </div>
  <div class="abs service" style="top:770px">
    <svg viewBox="0 0 44 40"><rect x="10" y="10" width="20" height="16" fill="var(--red)"/><path d="M30 14h7l5 6v6H30z" fill="var(--red)"/><rect x="2" y="13" width="6" height="2" fill="var(--red)"/><rect x="0" y="18" width="8" height="2" fill="var(--red)"/><rect x="3" y="23" width="5" height="2" fill="var(--red)"/><circle cx="16" cy="29" r="3.5" fill="var(--red)"/><circle cx="35" cy="29" r="3.5" fill="var(--red)"/></svg>
    <h3>LOGISTIC MANAGEMENT</h3>
    <p>From planning to delivery, our logistics consulting helps you make sense of your supply chain and find the best solutions.</p>
  </div>

  <footer class="abs site-footer" style="top:830px;height:312px">
    <div class="abs brand footer-brand" style="left:214px;top:24px"><span class="brand-dot"></span>Tandem R.R. Inc<br>Kansas City, KS</div>
    <div class="abs" style="left:43px;top:100px">
      <div class="f-label">CALL US</div><div class="f-value">555-014-2290</div>
      <div class="f-label" style="margin-top:17px">E-MAIL US</div><div class="f-value">enquire@tandemrr.example</div>
      <div class="f-label" style="margin-top:17px">REACH US</div><div class="f-value">718 Harlow Street<br>Kansas City, Kansas 66190</div>
    </div>
    <div class="abs f-links" style="left:381px;top:100px"><span>HOME</span><span>COMPANY</span><span>SERVICES</span><span>NEWS</span><span>CONTACT</span></div>
    <div class="abs social" style="left:381px;top:231px"><span></span><span></span><span></span></div>
  </footer>
</section>

<!-- ABOUT PAGE -->
<section class="page page--about">
  <header class="abs site-header">
    <div class="abs brand" style="left:36px;top:18px"><span class="brand-dot"></span>Tandem R.R.</div>
    <div class="abs contact-mini" style="left:212px;top:15px">
      <svg viewBox="0 0 10 10"><path d="M2 1l2 2-1 1.5c.6 1.2 1.4 2 2.5 2.5L7 6l2 2-1.3 1.3C4.5 9 1 5.5.7 2.3z" fill="none" stroke="#c41a12" stroke-width=".9"/></svg>
      <div>555-014-2290<br>enquire@tandemrr.example</div>
    </div>
    <div class="abs contact-mini" style="left:366px;top:15px">
      <svg viewBox="0 0 10 10"><path d="M5 9.5S1.8 6 1.8 4a3.2 3.2 0 016.4 0C8.2 6 5 9.5 5 9.5z" fill="none" stroke="#c41a12" stroke-width=".9"/><circle cx="5" cy="4" r="1.1" fill="#c41a12"/></svg>
      <div>718 Harlow Street<br>Kansas City, KS 66190</div>
    </div>
  </header>
  <nav class="abs main-nav">
    <div class="abs nav-links"><span class="active">HOME</span><span>COMPANY</span><span>SERVICES</span><span>NEWS</span><span>CONTACT</span></div>
    <div class="abs track" style="left:381px"><span>Enter Tracking ID</span><b>Track</b></div>
  </nav>

  <div class="abs about-hero" role="img" aria-label="Row of parked semi trucks at a depot, tinted dark blue"></div>
  <h1 class="abs about-title">ABOUT COMPANY</h1>

  <div class="abs about-body"></div>
  <h2 class="abs section-title" style="left:43px;top:220px;color:var(--red-text)">Our Company</h2>
  <div class="abs truck-photo" role="img" aria-label="Green cab box truck with white trailer"></div>
  <div class="abs about-copy">
    <p>Our transportation company with 30 years of experience is you best choice for shipping cargo of any size, storage, packing or delivering wares to your customers. Our professional employees will take care of your goods, whenever you send them.</p>
    <p>You are granted complete control over the process of delivery by phone or by our mobile app. Your freight is tracked every step of the way. We provide a high standard of shipping, regardless of its volume. If your company needs to establish a supply chain, we have prepared several readymade solutions with flexible pricing rates for you. Our urgent cargo services offer defined time frames for convenience of your business. Our supply chain services include shipping, warehousing, packaging, quality control and distribution.</p>
  </div>

  <div class="abs offer"></div>
  <h2 class="abs section-title" style="left:43px;top:487px;color:var(--white)">What We Offer</h2>
  <div class="abs offer-item" style="left:39px">
    <div class="icon"><svg width="22" height="22" viewBox="0 0 22 22"><circle cx="11" cy="5" r="3" fill="var(--red)"/><circle cx="4" cy="16" r="2.5" fill="var(--red)"/><circle cx="11" cy="16" r="2.5" fill="var(--red)"/><circle cx="18" cy="16" r="2.5" fill="var(--red)"/><path d="M11 8v5M4 13v-2h14v2" fill="none" stroke="var(--red)" stroke-width="1.2"/></svg></div>
    <h4>Team Spirit</h4>
    <p>We help each other, wherever we are. This makes work easier.</p>
  </div>
  <div class="abs offer-item" style="left:184px">
    <div class="icon"><svg width="24" height="24" viewBox="0 0 24 24"><path d="M20 12a8 8 0 11-3-6.2" fill="none" stroke="var(--red)" stroke-width="2"/><path d="M17 3v4h4" fill="none" stroke="var(--red)" stroke-width="2"/><text x="12" y="15" text-anchor="middle" font-size="8" font-weight="700" fill="var(--red)" font-family="Roboto,sans-serif">24</text></svg></div>
    <h4>24/7 Support</h4>
    <p>Our experts work day and night to solve all your cargo-related problems.</p>
  </div>
  <div class="abs offer-item" style="left:332px">
    <div class="icon"><svg width="22" height="22" viewBox="0 0 22 22"><rect x="5" y="4" width="12" height="15" rx="1" fill="var(--orange)"/><rect x="10" y="2" width="8" height="15" rx="1" fill="var(--red)"/></svg></div>
    <h4>Document Preparation</h4>
    <p>Our document maintenance methodology is dependable.</p>
  </div>

  <footer class="abs site-footer" style="top:646px;height:316px">
    <div class="abs brand footer-brand" style="left:214px;top:24px"><span class="brand-dot"></span>Tandem R.R. Inc<br>Kansas City, KS</div>
    <div class="abs" style="left:43px;top:98px">
      <div class="f-label">CALL US</div><div class="f-value">555-014-2290</div>
      <div class="f-label" style="margin-top:17px">E-MAIL US</div><div class="f-value">enquire@tandemrr.example</div>
      <div class="f-label" style="margin-top:17px">REACH US</div><div class="f-value">718 Harlow Street<br>Kansas City, Kansas 66190</div>
    </div>
    <div class="abs f-links" style="left:380px;top:98px"><span>HOME</span><span>COMPANY</span><span>SERVICES</span><span>NEWS</span><span>CONTACT</span></div>
    <div class="abs social" style="left:380px;top:198px"><span></span><span></span><span></span></div>
  </footer>
</section>

</body>
</html>
```